Business Card Design

Vintage looking Hair Salon, where the customer service is 100%. We are based in a cottage. With shabby chic console tables and beautiful ornate mirrors..and rich brown leather cutting chairs. Chandeliers at the window, and a ornate patchwork sofa.
our clientele are 28years upwards.. Mums with small children.. Ladies that lunch, and men that want more than a barbers and are prepared to pay for our services.
I am looking for a classy business card.. That look expensive.. Where our initials WMP become a visual reference.. I was thinking of cream card initials in black on a embossed tarnished silver.. But I'm open to suggestion. I want,  need the design to be able to work with flyers price list ect.

Industry/Entity Type
Business
Contact Information for Business Card
Willow Mane Parlour
17 Fernbrook Lane
Dunmore Green
bN42 6QW
FB thewillowmaneparlour
Info@thewilowmaneparlour.co.uk
0208 761 5924

```html
<!DOCTYPE html>
<html lang="en">
<head>
<meta charset="utf-8">
<title>Willow Mane Parlour – Business Card</title>
<link rel="stylesheet" href="https://fonts.googleapis.com/css2?family=Marcellus&family=Open+Sans:wght@400&display=swap">
<style>
  :root {
    --backdrop: #d8d0c2;
    --card-edge: #0c0c0c;
    --card-mid: #2a2a2a;
    --card-glow: #6a6a6a;
    --damask-tone: rgba(150, 150, 150, 0.16);
    --ornament-tone: rgba(120, 120, 120, 0.28);
    --ink: #f4f4f4;
  }
  * { margin: 0; padding: 0; box-sizing: border-box; }
  html, body {
    width: 1200px;
    height: 880px;
    overflow: hidden;
    background: var(--backdrop);
  }
  .canvas {
    width: 1200px;
    height: 880px;
    display: flex;
    align-items: center;
    justify-content: center;
  }
  .business-card {
    position: relative;
    width: 1000px;
    height: 572px;
    overflow: hidden;
    background: radial-gradient(ellipse 62% 60% at 50% 48%, var(--card-glow) 0%, var(--card-mid) 55%, var(--card-edge) 100%);
    box-shadow: 0 10px 30px rgba(0, 0, 0, 0.25);
  }
  .damask-field {
    position: absolute;
    inset: 0;
    background: radial-gradient(ellipse 70% 70% at 50% 50%, var(--damask-tone) 0%, rgba(150,150,150,0.06) 60%, transparent 100%);
  }
  .corner-ornament {
    position: absolute;
    width: 190px;
    height: 190px;
  }
  .corner-ornament--top-left { top: 0; left: 0; background: radial-gradient(circle at 0 0, var(--ornament-tone) 0%, transparent 70%); }
  .corner-ornament--top-right { top: 0; right: 0; background: radial-gradient(circle at 100% 0, var(--ornament-tone) 0%, transparent 70%); }
  .corner-ornament--bottom-left { bottom: 0; left: 0; background: radial-gradient(circle at 0 100%, var(--ornament-tone) 0%, transparent 70%); }
  .corner-ornament--bottom-right { bottom: 0; right: 0; background: radial-gradient(circle at 100% 100%, var(--ornament-tone) 0%, transparent 70%); }
  .card-content {
    position: absolute;
    inset: 0;
    display: flex;
    flex-direction: column;
    align-items: center;
    color: var(--ink);
    text-align: center;
  }
  .brand-name {
    margin-top: 92px;
    font-family: "Marcellus", serif;
    font-weight: 400;
    line-height: 1;
    text-shadow: 0 2px 4px rgba(0,0,0,0.5);
  }
  .brand-name__article { display: block; font-size: 40px; }
  .brand-name__main { display: block; font-size: 96px; margin-top: 4px; letter-spacing: 1px; }
  .brand-name__sub { display: block; font-size: 46px; margin-top: 2px; letter-spacing: 1px; }
  .contact-details {
    margin-top: 48px;
    font-family: "Open Sans", sans-serif;
    font-size: 27px;
    line-height: 1.45;
    font-style: normal;
  }
  .contact-details__divider { margin: 0 14px; }
</style>
</head>
<body>
<main class="canvas">
  <section class="business-card">
    <div class="damask-field" role="img" aria-label="Subtle grey damask swirl pattern across the card"></div>
    <div class="corner-ornament corner-ornament--top-left" role="img" aria-label="Ornate knotwork corner flourish"></div>
    <div class="corner-ornament corner-ornament--top-right" role="img" aria-label="Ornate knotwork corner flourish"></div>
    <div class="corner-ornament corner-ornament--bottom-left" role="img" aria-label="Ornate knotwork corner flourish"></div>
    <div class="corner-ornament corner-ornament--bottom-right" role="img" aria-label="Ornate knotwork corner flourish"></div>

    <div class="card-content">
      <h1 class="brand-name">
        <span class="brand-name__article">The</span>
        <span class="brand-name__main">Willow</span>
        <span class="brand-name__sub">Mane Parlour</span>
      </h1>
      <address class="contact-details">
        <div class="contact-details__address">17 Fernbrook Lane, Dunmore Green, BN42 6QW.</div>
        <div class="contact-details__online">E : Info@thewilowmaneparlour.co.uk<span class="contact-details__divider">|</span>FB : thewillowmaneparlour</div>
        <div class="contact-details__phone">PH : 0208 761 5924</div>
      </address>
    </div>
  </section>
</main>
</body>
</html>
```